Yacht Charter Broker needs a magazine page design

We are a travel agent for yachts called Velmoria Yacht Charters. www.velmoriacharters.example We are advertising in a magazine at the grand pacer equine fair - https://plgequinefair.example/ - and need a high-end luxury feeling magazine page.

Target Market(s)

Vacation goers looking to charter a crewed yacht.

Industry/Entity Type

Travel Agent

Requirements
Must have
• luxury feel. logo. website and social media icons if you feel necessary. Our motto is: Inhale. Exhale. Sail.
• Catamaran picture, snorkeling and other island, water looking pictures.
Nice to have
• Open to your design.
Should not have
• Nothing comes to mind.

```html
<!DOCTYPE html>
<html lang="en">
<head>
<meta charset="utf-8">
<title>Velmoria Yacht Charters – Magazine Page</title>
<link href="https://fonts.googleapis.com/css2?family=Cinzel:wght@400&family=Raleway:wght@200;400;500;800&display=swap" rel="stylesheet">
<style>
  :root {
    --ink: #0e0f13;
    --sea-deep: #0b3a6e;
    --sea-mid: #15528f;
    --sea-light: #1f67a8;
    --white: #ffffff;
  }
  html, body { margin: 0; padding: 0; overflow: hidden; }
  body { width: 1022px; height: 1200px; background: var(--ink); font-family: 'Raleway', sans-serif; color: var(--white); }
  .page { position: relative; width: 1022px; height: 1200px; overflow: hidden; }

  .masthead { position: absolute; left: 0; top: 0; width: 1022px; height: 192px; background: var(--ink); }
  .brand-name { position: absolute; left: 0; right: 0; top: 68px; text-align: center; font-family: 'Cinzel', serif; font-weight: 400; font-size: 58px; letter-spacing: 8px; line-height: 1; }
  .brand-tagline { position: absolute; left: 0; right: 0; top: 140px; text-align: center; font-family: 'Cinzel', serif; font-size: 14px; letter-spacing: 4px; }

  .hero { position: absolute; left: 0; top: 192px; width: 1022px; height: 725px; }
  .hero-photo { position: absolute; inset: 0; background: radial-gradient(ellipse at 28% 50%, var(--sea-light) 0%, var(--sea-mid) 45%, var(--sea-deep) 100%); }
  .hero-lines { position: absolute; inset: 0; }

  .motto { position: absolute; right: 90px; text-align: right; line-height: 1; margin: 0; }
  .motto-inhale { top: 34px; font-weight: 200; font-size: 116px; right: 100px; }
  .motto-exhale { top: 166px; font-weight: 200; font-size: 116px; }
  .motto-sail { top: 276px; font-weight: 800; font-size: 176px; letter-spacing: -2px; }

  .claim { position: absolute; left: 600px; width: 352px; top: 482px; text-align: center; font-weight: 500; font-size: 26px; line-height: 32px; margin: 0; }
  .intro { position: absolute; left: 0; top: 596px; width: 1022px; margin: 0; font-size: 17.5px; }
  .intro span { position: absolute; white-space: nowrap; }

  .closing { position: absolute; left: 70px; top: 956px; width: 882px; margin: 0; font-size: 17.5px; line-height: 26.5px; text-align: justify; text-align-last: center; }

  .social { position: absolute; top: 1106px; left: 710px; display: flex; gap: 20px; }
  .social-dot { width: 42px; height: 42px; border: 2px solid var(--white); border-radius: 50%; box-sizing: border-box; }
</style>
</head>
<body>
<div class="page">
  <header class="masthead">
    <div class="brand-name">VELMORIA</div>
    <div class="brand-tagline">YACHT CHARTER BROKER</div>
  </header>

  <section class="hero">
    <div class="hero-photo" role="img" aria-label="Aerial photo of a white catamaran under full sail crossing deep blue open sea, leaving a white wake"></div>
    <svg class="hero-lines" width="1022" height="725" viewBox="0 0 1022 725">
      <line x1="685" y1="220" x2="640" y2="360" stroke="#fff" stroke-width="4"/>
      <line x1="582" y1="482" x2="363" y2="725" stroke="#fff" stroke-width="4"/>
    </svg>
    <h1 class="motto motto-inhale">INHALE</h1>
    <h1 class="motto motto-exhale">EXHALE</h1>
    <h1 class="motto motto-sail">SAIL</h1>

    <h2 class="claim">VELMORIA IS THE WORLD'S FOREMOST IN YACHT CHARTERING</h2>
    <p class="intro">
      <span style="left:527px;top:0">Celebrities and the super rich have long used</span>
      <span style="left:505px;top:25px">yachts as a way of combining luxury and privacy,</span>
      <span style="left:482px;top:50px">and a growing market has seen it become not only</span>
      <span style="left:460px;top:75px">popular, but accessible, for those looking to</span>
      <span style="left:439px;top:100px">experience groundbreaking travel.</span>
    </p>
  </section>

  <p class="closing">Forget about the tight schedule of a cruise ship and dealing with multiple reservations of hotels and restaurants - Velmoria Yacht Charters offers an adventure like no other, with freedom AND flexibility. Custom-tailored to the exact vacation you and your guests want to experience, we also put together a professional crew dedicated to perfecting your experience. Luxury accomodations, relaxation like you've never felt, breathtaking views, gourmet cuisine and endless activities. Inhale, Exhale, Sail - with Velmoria Yacht Charters.</p>

  <nav class="social" aria-label="Social media">
    <div class="social-dot" role="img" aria-label="Social link"></div>
    <div class="social-dot" role="img" aria-label="Social link"></div>
    <div class="social-dot" role="img" aria-label="Social link"></div>
    <div class="social-dot" role="img" aria-label="Social link"></div>
  </nav>
</div>
</body>
</html>
```